Skin care manufacturer looking for packaging design for new skin care brand.

We need a design and logo for a skin care brand to be sold at retail stores and online in the United States and Europe. The design will be for 1.7oz - 2oz serums that will not have a retail box. The name of the brand is Orvia Lune and should be a luxurious brand that is approachable. The brand will consist of 4 face serums - Vitamin C, Collagen, Retinol and Hyaluronic Acid that all contain Dead Sea Minerals. Images shown are for inspiration only. Color of bottles can be varied based on design and bottles can be screen printed or labeled.

```html
<!DOCTYPE html>
<html lang="en">
<head>
<meta charset="utf-8">
<title>Orvia Lune — Face Serum Range</title>
<link href="https://fonts.googleapis.com/css2?family=Oswald:wght@500;600&family=Montserrat:wght@300;400&display=swap" rel="stylesheet">
<style>
  :root {
    --canvas: #f6f6f7;
    --cap: #f2f2f2;
    --cap-edge: #dcdcdc;
    --mineral-grey: #7f97a2;
    --label-ink: #2b2b2b;
    --white: #ffffff;

    --vitc-glass: #a9b4ec;
    --vitc-glass-deep: #7f8fd6;
    --vitc-mark: #3d9ad8;

    --collagen-glass: #ecbde0;
    --collagen-glass-deep: #d795c7;
    --collagen-mark: #c465b4;

    --retinol-glass: #f1c680;
    --retinol-glass-deep: #dc9d45;
    --retinol-mark: #c98b3a;

    --hyaluronic-glass: #a7dbeb;
    --hyaluronic-glass-deep: #5fa9c8;
    --hyaluronic-mark: #3f80a9;
  }

  * { box-sizing: border-box; margin: 0; padding: 0; }

  html, body {
    width: 1200px;
    height: 832px;
    overflow: hidden;
    background: var(--canvas);
  }

  .range {
    position: relative;
    width: 1200px;
    height: 832px;
  }

  .serum {
    position: absolute;
    top: 164px;
    width: 141px;
    height: 478px;
    margin-left: -70.5px;
  }
  .serum--vitc       { left: 125px;  --glass: var(--vitc-glass);       --glass-deep: var(--vitc-glass-deep);       --mark: var(--vitc-mark); }
  .serum--collagen   { left: 438px;  --glass: var(--collagen-glass);   --glass-deep: var(--collagen-glass-deep);   --mark: var(--collagen-mark); }
  .serum--retinol    { left: 750px;  --glass: var(--retinol-glass);    --glass-deep: var(--retinol-glass-deep);    --mark: var(--retinol-mark); }
  .serum--hyaluronic { left: 1063px; --glass: var(--hyaluronic-glass); --glass-deep: var(--hyaluronic-glass-deep); --mark: var(--hyaluronic-mark); }

  .dropper-bulb {
    position: absolute;
    left: 45px;
    top: 0;
    width: 51px;
    height: 93px;
    background: var(--cap);
    border: 1px solid var(--cap-edge);
    border-radius: 26px 26px 4px 4px;
  }
  .dropper-collar {
    position: absolute;
    left: 19px;
    top: 91px;
    width: 103px;
    height: 42px;
    background: var(--cap);
    border: 1px solid var(--cap-edge);
    border-radius: 4px;
  }

  .bottle-body {
    position: absolute;
    left: 0;
    top: 133px;
    width: 141px;
    height: 345px;
    border-radius: 6px 6px 16px 16px;
    background: linear-gradient(90deg, var(--glass-deep) 0%, var(--glass) 22%, #ffffff55 50%, var(--glass) 78%, var(--glass-deep) 100%), var(--glass);
  }

  .brand-name {
    position: absolute;
    top: 38px;
    left: 0;
    width: 100%;
    text-align: center;
    font-family: "Oswald", sans-serif;
    font-weight: 600;
    font-size: 40px;
    line-height: 40px;
    color: var(--mark);
    text-transform: uppercase;
  }

  .rule {
    position: absolute;
    left: 22px;
    width: 98px;
    height: 3px;
    background: var(--white);
  }
  .rule--top { top: 131px; }
  .rule--bottom { top: 195px; }

  .mineral-claim {
    position: absolute;
    top: 134px;
    left: 0;
    width: 100%;
    text-align: center;
    font-family: "Oswald", sans-serif;
    font-weight: 500;
    font-size: 22px;
    line-height: 26px;
    color: var(--mineral-grey);
    text-transform: uppercase;
  }

  .variant {
    position: absolute;
    left: 0;
    width: 100%;
    text-align: center;
    font-family: "Montserrat", sans-serif;
    font-weight: 400;
    font-size: 11.5px;
    line-height: 14px;
    letter-spacing: 0.3px;
    color: var(--label-ink);
    text-transform: uppercase;
  }
  .variant--single { top: 226px; }
  .variant--double { top: 213px; }
  .variant--collagen { font-size: 12.5px; line-height: 16px; font-weight: 300; }

  .product-type {
    position: absolute;
    top: 255px;
    left: 0;
    width: 100%;
    text-align: center;
    font-family: "Oswald", sans-serif;
    font-weight: 600;
    font-size: 15px;
    line-height: 19px;
    color: var(--white);
    text-transform: uppercase;
  }

  .volume {
    position: absolute;
    top: 311px;
    right: 24px;
    font-family: "Montserrat", sans-serif;
    font-weight: 300;
    font-size: 9.5px;
    color: var(--white);
  }
</style>
</head>
<body>
<main class="range">

  <article class="serum serum--vitc">
    <div class="dropper-bulb"></div>
    <div class="dropper-collar"></div>
    <div class="bottle-body">
      <h2 class="brand-name">Orvia<br>Lune</h2>
      <div class="rule rule--top"></div>
      <p class="mineral-claim">Dead Sea<br>Minerals</p>
      <div class="rule rule--bottom"></div>
      <p class="variant variant--single">Vitamin C</p>
      <p class="product-type">Brightening<br>Face Serum</p>
      <p class="volume">2fl. oz</p>
    </div>
  </article>

  <article class="serum serum--collagen">
    <div class="dropper-bulb"></div>
    <div class="dropper-collar"></div>
    <div class="bottle-body">
      <h2 class="brand-name">Orvia<br>Lune</h2>
      <div class="rule rule--top"></div>
      <p class="mineral-claim">Dead Sea<br>Minerals</p>
      <div class="rule rule--bottom"></div>
      <p class="variant variant--double variant--collagen">Collagen<br>Firming</p>
      <p class="product-type">Brightening<br>Face Serum</p>
      <p class="volume">2fl. oz</p>
    </div>
  </article>

  <article class="serum serum--retinol">
    <div class="dropper-bulb"></div>
    <div class="dropper-collar"></div>
    <div class="bottle-body">
      <h2 class="brand-name">Orvia<br>Lune</h2>
      <div class="rule rule--top"></div>
      <p class="mineral-claim">Dead Sea<br>Minerals</p>
      <div class="rule rule--bottom"></div>
      <p class="variant variant--double">Retinol<br>Anti-Wrinkle</p>
      <p class="product-type">Brightening<br>Face Serum</p>
      <p class="volume">2fl. oz</p>
    </div>
  </article>

  <article class="serum serum--hyaluronic">
    <div class="dropper-bulb"></div>
    <div class="dropper-collar"></div>
    <div class="bottle-body">
      <h2 class="brand-name">Orvia<br>Lune</h2>
      <div class="rule rule--top"></div>
      <p class="mineral-claim">Dead Sea<br>Minerals</p>
      <div class="rule rule--bottom"></div>
      <p class="variant variant--double">Hyaluronic Acid<br>Hydrating</p>
      <p class="product-type">Brightening<br>Face Serum</p>
      <p class="volume">2fl. oz</p>
    </div>
  </article>

</main>
</body>
</html>
```